Small Business Consulting Firm Needs Business Card Design

Need a sleek modern business card with 2 sides matching the colors of our logo. We will be placing these with a mailer we are sending out. These business cards will only ever be given to business owners. We operate helping businesses who are struggling with cash flow or finances. If the green and blue design needs to be moved to the right of "Harborline Crest Consulting" for aesthetic purposes that is ok. We will need an editable file if possible. We would like to include the reps name, email, website, and phone number. For now just use Peter Vance, pvance@harborlinecrest.com, www.harborlinecrest.com, and 833-555-0172.

```html
<!DOCTYPE html>
<html lang="en">
<head>
<meta charset="utf-8">
<title>Harborline Crest Consulting – Business Cards</title>
<link href="https://fonts.googleapis.com/css2?family=Open+Sans:wght@400;600&family=Montserrat:wght@700&display=swap" rel="stylesheet">
<style>
  :root {
    --stage: #e6e7e9;
    --brand-green: #639e38;
    --brand-blue: #0a7cc4;
    --ink: #3f4245;
    --ink-soft: #55585c;
    --paper: #ffffff;
  }
  * { box-sizing: border-box; margin: 0; padding: 0; }
  html, body { width: 1200px; height: 900px; overflow: hidden; }
  body {
    background: var(--stage);
    font-family: "Open Sans", Arial, sans-serif;
    position: relative;
  }
  .card {
    position: absolute;
    width: 640px;
    height: 366px;
    box-shadow: 0 14px 30px rgba(0,0,0,0.16), 0 2px 4px rgba(0,0,0,0.08);
  }
  .card--front { left: 80px; top: 60px; background: var(--brand-green); }
  .card--back  { left: 480px; top: 470px; background: var(--paper); }

  /* Wordmark */
  .wordmark { position: absolute; display: flex; align-items: center; gap: 14px; }
  .wordmark__square { flex: none; }
  .wordmark__text { font-weight: 400; line-height: 1.05; }
  .wordmark__name { display: block; letter-spacing: 0.02em; text-transform: uppercase; }
  .wordmark__tag  { display: block; letter-spacing: 0.42em; text-transform: uppercase; }

  .card--front .wordmark { left: 0; right: 0; top: 142px; justify-content: center; }
  .card--front .wordmark__text { color: var(--paper); }
  .card--front .wordmark__square { width: 46px; height: 46px; background: var(--paper); }
  .card--front .wordmark__name { font-size: 34px; }
  .card--front .wordmark__tag  { font-size: 17px; margin-top: 6px; padding-left: 4px; }

  .card--back .wordmark { right: 40px; top: 52px; }
  .card--back .wordmark__text { color: var(--ink); }
  .card--back .wordmark__square { width: 26px; height: 26px; background: var(--brand-green); }
  .card--back .wordmark__name { font-size: 19px; }
  .card--back .wordmark__tag  { font-size: 10px; margin-top: 4px; padding-left: 2px; }

  /* Rep block */
  .rep { position: absolute; left: 42px; top: 168px; }
  .rep__name { font-family: "Montserrat", Arial, sans-serif; font-weight: 700; font-size: 34px; line-height: 1; }
  .rep__first { color: var(--brand-blue); }
  .rep__last  { color: var(--brand-green); }
  .rep__role  { font-size: 17px; color: var(--ink-soft); margin-top: 2px; }

  .divider {
    position: absolute; left: 250px; right: 30px; top: 196px;
    height: 2px; background: var(--brand-green);
  }

  .contacts { position: absolute; left: 46px; top: 252px; list-style: none; }
  .contacts__item { display: flex; align-items: center; gap: 12px; font-size: 16px; color: var(--ink); height: 30px; }
  .contacts__icon { width: 20px; height: 20px; flex: none; }

  .address {
    position: absolute; right: 40px; top: 236px;
    text-align: right; font-size: 15px; line-height: 1.35; color: var(--ink);
  }
</style>
</head>
<body>

  <section class="card card--front" aria-label="Business card front">
    <div class="wordmark">
      <span class="wordmark__square"></span>
      <span class="wordmark__text">
        <span class="wordmark__name">Harborline Crest</span>
        <span class="wordmark__tag">Consulting</span>
      </span>
    </div>
  </section>

  <section class="card card--back" aria-label="Business card back">
    <div class="wordmark">
      <span class="wordmark__square"></span>
      <span class="wordmark__text">
        <span class="wordmark__name">Harborline Crest</span>
        <span class="wordmark__tag">Consulting</span>
      </span>
    </div>

    <div class="rep">
      <p class="rep__name"><span class="rep__first">Peter</span> <span class="rep__last">Vance</span></p>
      <p class="rep__role">owners</p>
    </div>
    <div class="divider"></div>

    <p class="address">Your location stree here<br>city name -81000</p>

    <ul class="contacts">
      <li class="contacts__item">
        <svg class="contacts__icon" viewBox="0 0 20 20" aria-hidden="true">
          <path d="M5 3l3 3-2 2c1 2 3 4 5 5l2-2 3 3-2 3C8 17 3 12 2 5z" fill="var(--brand-green)"/>
        </svg>
        833-555-0172
      </li>
      <li class="contacts__item">
        <svg class="contacts__icon" viewBox="0 0 20 20" aria-hidden="true">
          <rect x="2" y="4" width="16" height="12" fill="var(--brand-green)"/>
          <path d="M2 4l8 7 8-7" fill="none" stroke="#fff" stroke-width="1.5"/>
        </svg>
        pvance@harborlinecrest.com
      </li>
      <li class="contacts__item">
        <svg class="contacts__icon" viewBox="0 0 20 20" aria-hidden="true">
          <circle cx="10" cy="10" r="8" fill="none" stroke="var(--brand-green)" stroke-width="1.8"/>
          <ellipse cx="10" cy="10" rx="3.5" ry="8" fill="none" stroke="var(--brand-green)" stroke-width="1.4"/>
          <path d="M2 10h16" stroke="var(--brand-green)" stroke-width="1.4"/>
        </svg>
        www.harborlinecrest.com
      </li>
    </ul>
  </section>

</body>
</html>
```